Kelmora Legal Business Card

I require a corporate business card for a new legal services business.

I do not have a logo, nor do I want one.

I require a clean, neat a professional card for a law firm.

Details:

Business Name: Kelmora Legal
Name: Debra Lindqvist
Title: Corporate Services Manager
Location: Office 14 (Top Floor), Toravel Business Centre, Quinlan Grove Street, Alotau CBD, Milne Bay Province.
Postal Address: PO Box 593, Alotau, 211, Milne Bay Province, Papua New Guinea.
Contact: T: +675 6418250, F: +675 6413362, M: +675 72915867, E: dlindqvist@kelmoraexample.com.pg.

I look forward to your design submissions.

Industry/Entity Type

Legal

```html
<!DOCTYPE html>
<html lang="en">
<head>
<meta charset="utf-8">
<title>Kelmora Legal Business Card</title>
<link rel="stylesheet" href="https://fonts.googleapis.com/css2?family=Roboto+Condensed:wght@300;400&family=Open+Sans:wght@400&display=swap">
<style>
  :root {
    --backdrop: #fbf0da;
    --card-red: #a91c22;
    --panel-white: #ffffff;
    --ink-grey: #4a4a4a;
    --text-white: #ffffff;
  }
  html, body {
    margin: 0;
    padding: 0;
    width: 1200px;
    height: 900px;
    overflow: hidden;
    background: var(--backdrop);
  }
  .canvas {
    position: relative;
    width: 1200px;
    height: 900px;
  }
  .business-card {
    position: absolute;
    left: 180px;
    top: 210px;
    width: 840px;
    height: 480px;
    background: var(--card-red);
    box-shadow: 0 6px 18px rgba(0, 0, 0, 0.25);
    overflow: hidden;
  }
  .brand-panel {
    position: absolute;
    left: 24px;
    top: 18px;
    width: 240px;
    height: 240px;
    background: var(--panel-white);
    display: flex;
    flex-direction: column;
    align-items: center;
  }
  .brand-name {
    margin-top: 18px;
    font-family: "Roboto Condensed", sans-serif;
    font-weight: 400;
    font-size: 23px;
    letter-spacing: 1px;
    color: var(--card-red);
    text-transform: uppercase;
  }
  .brand-circle {
    margin-top: 14px;
  }
  .contact-panel {
    position: absolute;
    left: 0;
    top: 300px;
    width: 270px;
    height: 140px;
    background: var(--panel-white);
    padding: 14px 0 0 24px;
    box-sizing: border-box;
  }
  .contact-row {
    display: flex;
    align-items: center;
    gap: 10px;
    height: 36px;
    font-family: "Open Sans", sans-serif;
    font-size: 22px;
    color: var(--ink-grey);
  }
  .contact-icon {
    width: 24px;
    height: 24px;
    flex: none;
  }
  .person {
    position: absolute;
    right: 36px;
    top: 40px;
    text-align: right;
    color: var(--text-white);
    font-family: "Roboto Condensed", sans-serif;
  }
  .person-name {
    margin: 0;
    font-weight: 400;
    font-size: 38px;
    text-transform: uppercase;
    line-height: 1.1;
  }
  .person-title {
    margin: 4px 0 0;
    font-weight: 300;
    font-size: 27px;
  }
  .address {
    position: absolute;
    right: 36px;
    bottom: 30px;
    text-align: right;
    color: var(--text-white);
    font-family: "Roboto Condensed", sans-serif;
    font-weight: 300;
    font-size: 19px;
    line-height: 1.35;
    font-style: normal;
  }
</style>
</head>
<body>
<main class="canvas">
  <section class="business-card" aria-label="Kelmora Legal business card">
    <div class="brand-panel">
      <span class="brand-name">Kelmora Legal</span>
      <svg class="brand-circle" width="150" height="150" viewBox="0 0 150 150" aria-hidden="true">
        <circle cx="75" cy="75" r="68" fill="none" stroke="var(--card-red)" stroke-width="8"/>
      </svg>
    </div>

    <div class="contact-panel">
      <div class="contact-row">
        <svg class="contact-icon" viewBox="0 0 24 24" aria-label="Telephone">
          <path d="M3 9c0-3 4-5 9-5s9 2 9 5v2h-5V9c-1-1-7-1-8 0v2H3z" fill="var(--card-red)"/>
          <path d="M6 13h12l2 8H4z" fill="var(--card-red)"/>
          <circle cx="12" cy="17" r="2" fill="#fff"/>
        </svg>
        <span>675 6418250</span>
      </div>
      <div class="contact-row">
        <svg class="contact-icon" viewBox="0 0 24 24" aria-label="Fax">
          <rect x="6" y="2" width="12" height="8" fill="none" stroke="var(--card-red)" stroke-width="2"/>
          <rect x="3" y="9" width="18" height="13" rx="2" fill="var(--card-red)"/>
          <rect x="7" y="13" width="10" height="2" fill="#fff"/>
          <rect x="7" y="17" width="10" height="2" fill="#fff"/>
        </svg>
        <span>675 6413362</span>
      </div>
      <div class="contact-row">
        <svg class="contact-icon" viewBox="0 0 24 24" aria-label="Mobile">
          <rect x="7" y="2" width="10" height="20" rx="2" fill="var(--card-red)"/>
          <rect x="9" y="5" width="6" height="6" fill="#fff"/>
          <rect x="9" y="13" width="6" height="6" fill="#fff" opacity="0.6"/>
        </svg>
        <span>675 72915867</span>
      </div>
    </div>

    <header class="person">
      <h1 class="person-name">Debra Lindqvist</h1>
      <p class="person-title">Corporate Services Manager</p>
    </header>

    <address class="address">
      Office 14 (Top Floor), Toravel Business Centre,<br>
      Quinlan Grove Street, Alotau CBD, Milne Bay Province.<br>
      PO Box 593, Alotau, 211, Milne Bay Province, Papua New Guinea<br>
      dlindqvist@kelmoraexample.com.pg
    </address>
  </section>
</main>
</body>
</html>
```